Online-Marketing Material für medizinischen Online Ratgeber
Zielgruppe
Die Welt der Thoraxmedizin kann komplex und verwirrend sein. Orvena Linde steht für kompetente Beratung und verlässliche Informationen rund um das Thema Thoraxerkrankungen – entstanden aus dem Wunsch, umfassende Informationen zur Verfügung zu stellen Ob Lungenkrebs, Asthma, COPD oder Schlafapnoe – wir bringen Klarheit in alle Aspekte der ThoraxmedizinThorax Schweiz ist nicht nur eine Informationsplattform, sondern auch eine Gemeinschaft, in der jeder willkommen und eingeladen ist, Fragen zu stellen, sein Wissen zu erweitern und zu teilen.
Aufgabenstellung
Orvena Linde ist ein online Ratgeber im Bereich der thorax Erkrankungen. wir wollen mit dem facebook Auftritt die Webseite ergänzen.Wir benötigen für facebook ein Profilbanner (1200x630), ein Profilbild 800x800) sowie einen Entwurf für ein posting(800x800). Die Farben die verwendet werden solltenund das Logo von orvena linde habe ich im Anhang beigefügt.Ich bedanke mich schon jetzt für Ihre Mühe und freue mich auf Ihre Entwürfe.

```html
<!DOCTYPE html>
<html lang="de">
<head>
<meta charset="utf-8">
<title>Orvena Linde – Social Media Set</title>
<link rel="stylesheet" href="https://fonts.googleapis.com/css2?family=Bebas+Neue&family=Roboto+Condensed:wght@700&family=Roboto:wght@700&display=swap">
<style>
  :root {
    --navy: #173a6c;
    --brand-blue: #0a96d6;
    --ring-blue: #1d96d8;
    --ice-light: #cfe8f1;
    --ice-mid: #8ec3d6;
    --ice-deep: #5f9fb8;
    --white: #ffffff;
  }
  html, body {
    margin: 0;
    padding: 0;
    width: 1200px;
    height: 848px;
    overflow: hidden;
    background: var(--white);
  }
  .canvas {
    position: relative;
    width: 1200px;
    height: 848px;
  }
  .cover-banner {
    position: absolute;
    left: 238px;
    top: 73px;
    width: 679px;
    height: 356px;
    overflow: hidden;
  }
  .cover-photo {
    position: absolute;
    inset: 0;
    background:
      radial-gradient(ellipse 38% 70% at 72% 62%, rgba(230,245,250,0.85), rgba(180,220,235,0.35) 60%, transparent 80%),
      linear-gradient(100deg, var(--ice-deep) 0%, var(--ice-light) 35%, var(--ice-mid) 70%, var(--ice-deep) 100%);
  }
  .cover-headline {
    position: absolute;
    margin: 0;
    font-family: "Bebas Neue", sans-serif;
    font-weight: 400;
    font-size: 55px;
    line-height: 1;
    color: var(--navy);
    letter-spacing: 0.5px;
  }
  .cover-headline .line-one { position: absolute; left: 83px; top: 123px; white-space: nowrap; }
  .cover-headline .line-two { position: absolute; left: 166px; top: 177px; white-space: nowrap; }
  .profile-badge {
    position: absolute;
    left: 297px;
    top: 360px;
    width: 158px;
    height: 158px;
    border-radius: 50%;
    border: 4px solid var(--ring-blue);
    background: var(--white);
    display: flex;
    align-items: center;
    justify-content: center;
    text-align: center;
  }
  .profile-name {
    font-family: "Roboto", sans-serif;
    font-weight: 700;
    font-size: 25px;
    line-height: 0.95;
    color: var(--navy);
    margin: 0;
  }
  .fact-post {
    position: absolute;
    left: 533px;
    top: 463px;
    width: 331px;
    height: 331px;
    background: var(--brand-blue);
    font-family: "Roboto Condensed", sans-serif;
    font-weight: 700;
    color: var(--white);
    text-align: center;
  }
  .fact-label {
    position: absolute;
    left: 84px;
    top: 62px;
    width: 155px;
    height: 28px;
    background: var(--navy);
    font-size: 19px;
    line-height: 28px;
  }
  .fact-text {
    position: absolute;
    left: 0;
    right: 0;
    top: 97px;
    margin: 0;
    font-size: 45px;
    line-height: 42px;
    letter-spacing: -0.3px;
  }
  .fact-text .highlight { color: var(--navy); }
  .fact-brand {
    position: absolute;
    left: 0;
    right: 0;
    top: 293px;
    font-family: "Roboto", sans-serif;
    font-size: 17px;
    line-height: 1;
    letter-spacing: 0.2px;
  }
</style>
</head>
<body>
<main class="canvas">
  <section class="cover-banner">
    <div class="cover-photo" role="img" aria-label="Hellblaue, leuchtende Darstellung eines menschlichen Oberkörpers mit sichtbarer Lunge und Bronchien"></div>
    <h1 class="cover-headline">
      <span class="line-one">Der Ratgeber für</span>
      <span class="line-two">Thoraxpatienten</span>
    </h1>
  </section>

  <div class="profile-badge">
    <p class="profile-name">ORVENA<br>LINDE</p>
  </div>

  <section class="fact-post">
    <div class="fact-label">Schon gewußt?</div>
    <p class="fact-text">Lorem ipsum<br>est durum <span class="highlight">80%</span><br>fertet dolu.</p>
    <div class="fact-brand">ORVENA LINDE</div>
  </section>
</main>
</body>
</html>
```